Donations Website - Fund page design

We need an on brand fund page for our crowdfunding website. The design should keep in mind Quillmark Framegrid 3 default columns and spacing.

Please use this development site as a guide... ( under construction )
http://lenor.pursivo-example.com:8080/

Elements to include:
• Framegrid 3 default column layout ( based on 12 column / 1140px / 30px gutters )
• Fund title ( Default Page Fund Title )
• Fund image / video ( 16:9 ratio )
• Fund progress: Current $ amount, Goal $ amount, # donations, # supporters, # views, % progress, progress bar, # shares
• Share buttons ( Chatterloop, Murmurly, Zentrix+, WorkNestle, Snapboardly, Email )
• Donate button
• Sections for ( Fund story, fund updates and fund comments... could be tabbed )
• Section for recent donations (name + cl photo / icon + anonymous / donation amount, short message )
• Button to report this fund
• Fund created by section ( name, chatterloop photo if they've verified using chatterloop and number of friends )
• Contact fund raiser button/link
Updates

The design brief has been updated. I've attached the logo as well, please use unless you feel you have something better to include.

Thanks.

I can't stress enough that this is 'NOT' a home page design. This is a personal fund page for a single user. Please do not include 'Other funds' on this page to promote.

Thanks,

Edvin

The page should be similar to these pages. As you can see, these are single fund pages within these sites. I do not want my page to look like these, but have the features I included in the brief while fitting my site's design.

http://www.pledgora-example.com/4qa8rb
https://www.launchvane-example.com/projects/502719846/lumo-crest?ref=home_location
http://www.fundquarry-example.com/projects/the-amber-harborfolk

Thanks,

Edvin

Target Market(s)

Adults age 18-50 mainly. Anyone that potentially needs to raise money.

Industry/Entity Type

Construction

Font styles to use
Sans Serif

Colors

Designer to choose colors to be used in the design.

Requirements
Must have
• • Framegrid 3 default column layout ( based on 12 column / 1140px / 30px gutters )
• Donate button
Nice to have
• Would be nice to keep in mind that users may be able to choose a theme color during fund setup. But if the design is strong enough on its own we will not include this option.

```html
<!DOCTYPE html>
<html lang="en">
<head>
<meta charset="utf-8">
<title>Kindrise – Fund Page</title>
<link href="https://fonts.googleapis.com/css2?family=Lobster&family=Open+Sans:wght@400;600;700&display=swap" rel="stylesheet">
<style>
:root{
  --paper:#eceae2;
  --paper-dark:#e4e1d6;
  --teal:#4a9e98;
  --teal-dark:#3a8680;
  --slate:#58657a;
  --slate-dark:#3d4655;
  --ink:#3f3f3f;
  --muted:#6b6b6b;
  --gold:#d9cb8b;
  --amount:#e9c24a;
  --white:#ffffff;
}
*{box-sizing:border-box;margin:0;padding:0}
html,body{width:810px;height:1200px;overflow:hidden}
body{background:var(--paper);font-family:"Open Sans",sans-serif;color:var(--ink);position:relative}
.abs{position:absolute}

/* header */
.site-header{left:0;top:0;width:810px;height:50px;background:#efede6;box-shadow:0 1px 3px rgba(0,0,0,.12)}
.brand{left:80px;top:14px;display:flex;align-items:center;gap:6px;font-weight:700;font-size:15px;color:#3d3d3d;letter-spacing:.5px}
.brand-dot{width:18px;height:18px;border-radius:50%;background:#3d3d3d}
.main-nav{left:379px;top:20px;display:flex;font-size:9px;color:#555;letter-spacing:.2px;white-space:nowrap}
.main-nav span{padding:0 9px;border-left:1px solid #bbb;line-height:10px}
.main-nav span:first-child{border-left:0;padding-left:0}
.btn-sm{top:11px;height:27px;border-radius:4px;color:#fff;font-size:9px;font-weight:700;display:flex;align-items:center;justify-content:center;white-space:nowrap}
.btn-signup{left:622px;width:52px;background:var(--slate-dark)}
.btn-login{left:679px;width:52px;background:var(--teal)}

/* hero */
.hero-title{left:0;width:810px;top:72px;text-align:center;font-family:"Lobster",cursive;font-size:40px;color:var(--teal)}
.hero-sub{left:0;width:810px;top:126px;text-align:center;font-size:13px;letter-spacing:1.3px;color:#444}

.card{background:#e6e3d9;border:1px solid #d6d2c5;box-shadow:0 0 0 4px #f1efe8 inset}
.video-card{left:78px;top:171px;width:381px;height:217px}
.video{left:85px;top:178px;width:368px;height:204px;background:linear-gradient(135deg,#5d4a3a,#c8a98a 45%,#8f8a80 70%,#3a3530)}
.video-controls{left:85px;top:362px;width:368px;height:20px;background:#1f1f1f;color:#ccc;font-size:7px;display:flex;align-items:center;padding-left:50px}
.play{left:232px;top:234px}

.creator-card{left:478px;top:171px;width:252px;height:217px}
.creator-photo{left:496px;top:200px;width:98px;height:98px;border:4px solid #f4f2ec;background:linear-gradient(#8fb4d8,#d9b89a);box-shadow:0 1px 2px rgba(0,0,0,.2)}
.creator-label{left:602px;top:199px;font-size:11px;color:#555}
.creator-name{left:602px;top:213px;font-size:12px;color:var(--teal)}
.friends{left:602px;top:238px;font-size:10px;color:#444;display:flex;align-items:center;gap:6px;white-space:nowrap}
.friends b{font-weight:700}
.btn-contact{left:600px;top:266px;width:112px;height:32px;background:#ece9e0;border:1px solid #d8d4c8;border-radius:4px;font-size:8.5px;font-weight:700;color:#444;display:flex;align-items:center;justify-content:center;white-space:nowrap}
.btn-donate{left:496px;top:319px;width:216px;height:48px;background:linear-gradient(#5fb1aa,#45958f);border-radius:5px;color:#fff;font-size:18px;font-weight:600;letter-spacing:.5px;display:flex;align-items:center;justify-content:center;gap:12px;padding-left:18px;white-space:nowrap;box-shadow:0 2px 0 #387c77}
.btn-donate svg{flex:none}

/* stats band */
.stats-band{left:0;top:437px;width:810px;height:81px;background:var(--slate)}
.band-rule{left:0;top:518px;width:810px;height:3px;background:var(--slate-dark)}
.stat-box{top:414px;height:46px;background:var(--slate-dark);border-top:2px dashed #8e96a3;border-bottom:2px dashed #8e96a3;color:#fff;font-size:14px;display:flex;align-items:center;justify-content:center;gap:4px;white-space:nowrap}
.stat-box b{color:var(--amount);font-weight:600}
.raised{left:80px;width:182px}
.goal{left:277px;width:181px}
.progress-box{left:478px;top:414px;width:252px;height:46px;background:var(--gold);border-top:2px dashed #c3b46f;border-bottom:2px dashed #c3b46f;padding:6px 11px}
.progress-label{font-size:12px;color:#4e4a3a}
.progress-label b{color:var(--teal-dark)}
.bar{margin-top:3px;height:9px;border-radius:5px;background:#a9d4cf;border:1px solid #3e8a84;overflow:hidden}
.bar i{display:block;width:90%;height:100%;background:var(--teal-dark)}
.counts{left:80px;top:480px;display:flex;gap:14px;font-size:10px;color:#fff;align-items:center;white-space:nowrap}
.counts b{color:#8fcfc8;font-weight:400}
.counts .item{display:flex;align-items:center;gap:5px}
.btn-report{left:363px;top:470px;width:95px;height:36px;background:#ece9e0;border-radius:4px;font-size:9px;font-weight:700;color:#444;display:flex;align-items:center;justify-content:center;white-space:nowrap}
.shares{left:477px;top:478px;display:flex;gap:3px}
.share{width:40px;text-align:center}
.share-btn{height:14px;background:#fff;border:1px solid #bbb;border-radius:2px;font-size:7px;color:#444;display:flex;align-items:center;justify-content:center;gap:2px}
.share-btn i{width:7px;height:7px;background:#555;display:block}
.share-count{color:#fff;font-size:10px;margin-top:3px}

/* tabs & story */
.tabs{left:78px;top:569px;display:flex;gap:3px}
.tab{width:99px;height:29px;background:#e3e0d6;border:1px solid #d4d0c4;border-bottom:0;font-size:9px;font-weight:700;color:#444;display:flex;align-items:center;justify-content:center;white-space:nowrap}
.tab.active{background:#fff}
.story{left:78px;top:597px;width:444px;height:519px;background:#fff;padding:18px 21px;border-radius:0 4px 4px 4px;box-shadow:0 1px 2px rgba(0,0,0,.06)}
.story h1{font-family:"Lobster",cursive;font-weight:400;font-size:17px;color:var(--teal);margin-bottom:10px}
.story p{font-size:10.2px;line-height:15.2px;color:var(--muted)}
.story p b{font-weight:600;color:#555}
.story p u{color:#555}
.story h2{font-size:10.6px;font-weight:700;color:var(--teal-dark);margin-top:14px;line-height:15px}
.story-media{float:left;width:178px;height:112px;margin:2px 12px 8px 0;background:linear-gradient(#2a2a2a,#111);border-radius:6px;padding:7px 8px}
.story-media div{width:100%;height:100%;background:linear-gradient(#f4f6f8,#dfe6ec)}

/* donations */
.donations-title{left:541px;top:549px;font-family:"Lobster",cursive;font-size:19px;color:var(--teal);white-space:nowrap}
.donations-sub{left:541px;top:574px;font-size:10px;color:#555;white-space:nowrap}
.donation{left:541px;width:189px;height:134px;border-bottom:1px solid #d6d2c6}
.donor-photo{left:0;top:0;width:72px;height:60px;border:3px solid #fff;box-shadow:0 1px 2px rgba(0,0,0,.2)}
.donor-name{left:82px;top:0;font-size:10px;font-weight:700;color:#444;white-space:nowrap}
.donor-amount{left:81px;top:11px;font-size:30px;font-weight:400;color:var(--teal);letter-spacing:-.5px}
.donor-time{left:83px;top:54px;font-size:9px;color:#555}
.donor-msg{left:0;top:72px;width:189px;font-size:8.8px;line-height:13.6px;color:#444;padding-left:21px}
.donor-msg::before{content:"\201C";position:absolute;left:1px;top:-3px;font-size:18px;color:#555;font-family:Georgia,serif}

.site-footer{left:0;top:1158px;width:810px;height:42px;background:var(--slate);color:#fff;font-size:9px;display:flex;align-items:center;justify-content:center}
</style>
</head>
<body>

<header class="site-header abs">
  <div class="brand abs"><span class="brand-dot"></span>KINDRISE</div>
  <nav class="main-nav abs"><span>HOW IT WORKS</span><span>FAQS</span><span>SUPPORT</span><span>ABOUT</span></nav>
  <div class="btn-sm btn-signup abs">SIGN UP</div>
  <div class="btn-sm btn-login abs">LOGIN</div>
</header>

<div class="hero-title abs">Crowdfunding For Everyone</div>
<div class="hero-sub abs">Because everyone has a dream!</div>

<div class="video-card card abs"></div>
<div class="video abs" role="img" aria-label="Fund video still: a smiling couple looking at a laptop"></div>
<svg class="play abs" width="74" height="74" viewBox="0 0 74 74"><circle cx="37" cy="37" r="37" fill="rgba(20,20,20,.55)"/><path d="M31 28 L45 37 L31 46Z" fill="#bbb"/></svg>
<div class="video-controls abs">00:00 / 10:46</div>

<div class="creator-card card abs"></div>
<div class="creator-photo abs" role="img" aria-label="Profile photo of the fund creator"></div>
<div class="creator-label abs">Fund Created by:</div>
<div class="creator-name abs">Marlo Fenwick</div>
<div class="friends abs">
  <svg width="20" height="16" viewBox="0 0 20 16"><circle cx="8" cy="5" r="4" fill="none" stroke="#7a9bc4" stroke-width="1.3"/><path d="M1 16c0-5 3-6 7-6s7 1 7 6" fill="none" stroke="#7a9bc4" stroke-width="1.3"/></svg>
  Friends - <b>569</b>
</div>
<div class="btn-contact abs">Contact Fund Raiser</div>
<div class="btn-donate abs"><span>DONATE NOW</span>
  <svg width="30" height="27" viewBox="0 0 30 27"><path d="M15 27 L2 13 A7.5 7.5 0 0 1 15 4 A7.5 7.5 0 0 1 28 13Z" fill="#2f4750"/></svg>
</div>

<div class="stats-band abs"></div>
<div class="band-rule abs"></div>
<div class="stat-box raised abs">Raised: <b>$45,000.00</b></div>
<div class="stat-box goal abs">Goal: <b>$50,000.00</b></div>
<div class="progress-box abs">
  <div class="progress-label">Fund Progress: <b>90%</b></div>
  <div class="bar"><i></i></div>
</div>
<div class="counts abs">
  <span class="item"><svg width="11" height="10" viewBox="0 0 30 27"><path d="M15 27 L2 13 A7.5 7.5 0 0 1 15 4 A7.5 7.5 0 0 1 28 13Z" fill="#f0d98a"/></svg>Donations : <b>121</b></span>
  <span class="item"><svg width="11" height="11" viewBox="0 0 12 12"><circle cx="6" cy="6" r="5" fill="none" stroke="#ddd" stroke-width="2"/><circle cx="6" cy="6" r="2" fill="#ddd"/></svg>Support : <b>560</b></span>
  <span class="item"><svg width="13" height="9" viewBox="0 0 14 9"><path d="M1 4.5C4 0 10 0 13 4.5C10 9 4 9 1 4.5Z" fill="#ddd"/><circle cx="7" cy="4.5" r="2" fill="#58657a"/></svg>Views : <b>1456</b></span>
</div>
<div class="btn-report abs">Report this Fund</div>
<div class="shares abs">
  <div class="share"><div class="share-btn"><i></i>Share</div><div class="share-count">307</div></div>
  <div class="share"><div class="share-btn"><i></i>Share</div><div class="share-count">14</div></div>
  <div class="share"><div class="share-btn"><i></i>Share</div><div class="share-count">3</div></div>
  <div class="share"><div class="share-btn"><i></i>Share</div><div class="share-count">65</div></div>
  <div class="share"><div class="share-btn"><i></i>Share</div><div class="share-count">0</div></div>
  <div class="share"><div class="share-btn"><i></i>Email</div><div class="share-count">0</div></div>
</div>

<div class="tabs abs">
  <div class="tab active">Fund Story</div>
  <div class="tab">Fund Updates</div>
  <div class="tab">Fund Comments</div>
</div>
<article class="story abs">
  <h1>Lorem ipsum dolor sit amet</h1>
  <div class="story-media"><div role="img" aria-label="Tablet showing a dashboard with bar and line charts"></div></div>
  <p>Sed quis nisi euismod, fermentum tellus a, lobortis quam. Vestibulum condimentum mi vitae diam tristique, egestas dignissim diam mattis. Curabitur vel diam in massa porttitor dictum id in lorem. <u>Vivamus faucibus</u> ac leo ac dignissim. Maecenas orci est, euismod facilisis feugiat sit amet, semper ut tortor. Donec eleifend accumsan nisl, nec laoreet leo iaculis sit amet. <b>Vivamus varius</b> arcu eu hendrerit. Vivamus eu magna rhoncus, consectetur metus ac, varius lacus. Donec ultricies, tortor quis sagittis sagittis, mauris erat ullamcorper augue, eu placerat diam nunc a lorem.</p>
  <h2>Nam vulputate mauris id arcu pharetra</h2>
  <p>Sed posuere quam cursus. Nullam eget massa vel mi posuere venenatis sed quis tortor. In hac habitasse platea dictumst. Fusce nisi tellus, fermentum a luctus eget, convallis vitae orci. In commodo egestas magna quis placerat. Quisque adipiscing consequat nisi, nec accumsan quam venenatis ac.</p>
  <h2>Fusce quam dui, accumsan a magna in</h2>
  <p>Nullam eget massa vel mi posuere venenatis sed quis tortor. In hac habitasse platea dictumst. Fusce nisi tellus, fermentum a luctus eget, convallis vitae orci. In commodo egestas magna quis placerat.</p>
  <h2>Nam vulputate mauris id arcu pharetra</h2>
  <p>Sed posuere quam cursus. Nullam eget massa vel mi posuere venenatis sed quis tortor. In hac habitasse platea dictumst. Fusce nisi tellus, fermentum a luctus eget, convallis vitae orci. In commodo egestas magna quis placerat. Quisque adipiscing consequat nisi, nec accumsan quam venenatis ac.</p>
</article>

<div class="donations-title abs">Recent Donations (234)</div>
<div class="donations-sub abs">$45,000.00 raised in 12 days</div>

<div class="donation abs" style="top:598px">
  <div class="donor-photo abs" role="img" aria-label="Donor photo" style="background:linear-gradient(#f2f2f2,#d9b59a)"></div>
  <div class="donor-name abs">Oren Battaly</div>
  <div class="donor-amount abs">$150</div>
  <div class="donor-time abs">25 mins ago</div>
  <div class="donor-msg abs">Lorem ipsum dolor sit amet, consectetur adipiscing elit. Sed quis nisi euismod, fermentum tellus a, lobortis quam.</div>
</div>
<div class="donation abs" style="top:732px">
  <div class="donor-photo abs" role="img" aria-label="Donor photo" style="background:linear-gradient(#8aa05a,#d9b08e)"></div>
  <div class="donor-name abs">Huxley Dane</div>
  <div class="donor-amount abs">$160</div>
  <div class="donor-time abs">2 hours ago</div>
  <div class="donor-msg abs">Donec eleifend accumsan nisl, nec laoreet leo iaculis sit amet. Vivamus varius arcu eu sagittis aliquam.</div>
</div>
<div class="donation abs" style="top:866px">
  <div class="donor-photo abs" role="img" aria-label="Donor photo" style="background:linear-gradient(#9bb36a,#d4a77e)"></div>
  <div class="donor-name abs">Calder Moss</div>
  <div class="donor-amount abs">$250</div>
  <div class="donor-time abs">2 days ago</div>
  <div class="donor-msg abs">Vivamus varius arcu eu sagittis aliquam. Donec eleifend accumsan nisl, nec laoreet leo iaculis sit amet.</div>
</div>
<div class="donation abs" style="top:1000px">
  <div class="donor-photo abs" role="img" aria-label="Donor photo" style="background:linear-gradient(#3a2a22,#a06f4f)"></div>
  <div class="donor-name abs">Ilsa Verhoven</div>
  <div class="donor-amount abs">$100</div>
  <div class="donor-time abs">2 days ago</div>
  <div class="donor-msg abs">Vivamus varius arcu eu sagittis aliquam. Donec eleifend accumsan nisl, nec laoreet leo iaculis sit amet.</div>
</div>

<footer class="site-footer abs">© 2014 Kindrise. All rights reserved.</footer>

</body>
</html>
```